New Business Cards for MB&LR

We need updated business cards for a staff of 15 engineers, estimators, project managers, and sales people. We have recently begun changes to our website and marketing material to improve our look and branding. We are an established fabricator specializing in pressure vessels, tanks, and structural steel. The owners require us to use the existing logo and old english text design. Also, we prefer dark grey or mostly black cards.
Target Market(s)
Engineers, purchasing agents, estimators, and project managers of; mining companies, refineries, industrial construction professionals
Industry/Entity Type
Business
Contact Information for Business Card
Logo, phone, website, email, etc.
Look and feel

```html
<!DOCTYPE html>
<html lang="en">
<head>
<meta charset="utf-8">
<title>MB&amp;LR Business Card</title>
<link href="https://fonts.googleapis.com/css2?family=UnifrakturMaguntia&family=Oswald:wght@700&family=Montserrat:wght@400&display=swap" rel="stylesheet">
<style>
  :root {
    --bg: #e9e6e1;
    --card-dark: #464648;
    --card-light: #f6f6f4;
    --ink-dark: #1c1c1c;
    --ink-light: #f2f2f2;
  }
  * { box-sizing: border-box; margin: 0; padding: 0; }
  html, body { width: 1200px; height: 1000px; overflow: hidden; }
  body {
    background: var(--bg);
    position: relative;
    font-family: "Montserrat", sans-serif;
  }
  .card {
    position: absolute;
    left: 220px;
    width: 760px;
    height: 434px;
    display: flex;
    box-shadow: 0 10px 28px rgba(0,0,0,0.18);
    overflow: hidden;
  }
  .card--contact { top: 48px; }
  .card--front { top: 518px; }

  /* Contact side */
  .contact__brand {
    width: 36%;
    background: var(--card-light);
    padding: 60px 18px 0 18px;
    color: var(--ink-dark);
    display: flex;
    flex-direction: column;
    align-items: center;
  }
  .brand-mark {
    display: flex;
    align-items: center;
    gap: 12px;
    font-family: "Oswald", sans-serif;
    font-weight: 700;
    font-size: 38px;
    letter-spacing: 1px;
    white-space: nowrap;
  }
  .brand-mark__dot {
    width: 18px; height: 18px;
    border-radius: 50%;
    background: var(--ink-dark);
  }
  .tagline {
    margin-top: 56px;
    font-family: "UnifrakturMaguntia", cursive;
    font-size: 30px;
    line-height: 1.5;
    text-align: center;
    white-space: nowrap;
  }
  .contact__details {
    flex: 1;
    background: var(--card-dark);
    color: var(--ink-light);
    padding: 120px 40px 0 0;
    display: flex;
    flex-direction: column;
    gap: 46px;
  }
  .detail {
    display: flex;
    justify-content: flex-end;
    align-items: center;
    gap: 34px;
    font-size: 17px;
    letter-spacing: 1.5px;
    white-space: nowrap;
  }
  .detail svg { width: 24px; height: 24px; flex: none; }

  /* Front side */
  .front__dark { width: 49%; background: var(--card-dark); }
  .front__light {
    flex: 1;
    background: var(--card-light);
    display: flex;
    align-items: center;
    padding-left: 40px;
  }
  .front__light .brand-mark { font-size: 58px; color: var(--ink-dark); }
  .front__light .brand-mark__dot { width: 26px; height: 26px; }
</style>
</head>
<body>

  <section class="card card--contact">
    <div class="contact__brand">
      <div class="brand-mark"><span class="brand-mark__dot"></span>MB&amp;LR</div>
      <p class="tagline">Pressure Vessel<br>&amp;<br>Tank Works</p>
    </div>
    <div class="contact__details">
      <div class="detail">
        <span>555.310.4827 / 555.310.6195</span>
        <svg viewBox="0 0 24 24" fill="none" stroke="currentColor" stroke-width="2" stroke-linecap="round" stroke-linejoin="round"><path d="M6 3h3l2 5-2.5 1.5a11 11 0 0 0 6 6L16 13l5 2v3a2 2 0 0 1-2 2A16 16 0 0 1 4 5a2 2 0 0 1 2-2z"/></svg>
      </div>
      <div class="detail">
        <span>www.mbandlr-fab.com</span>
        <svg viewBox="0 0 24 24" fill="none" stroke="currentColor" stroke-width="2"><circle cx="12" cy="12" r="9"/><path d="M3 12h18M12 3c3 3 3 15 0 18M12 3c-3 3-3 15 0 18"/></svg>
      </div>
      <div class="detail">
        <span>275 Harbor Row Millbrook 40210</span>
        <svg viewBox="0 0 24 24" fill="none" stroke="currentColor" stroke-width="2"><path d="M12 21s-6-6.5-6-11a6 6 0 0 1 12 0c0 4.5-6 11-6 11z"/><circle cx="12" cy="10" r="2.2"/></svg>
      </div>
    </div>
  </section>

  <section class="card card--front">
    <div class="front__dark"></div>
    <div class="front__light">
      <div class="brand-mark"><span class="brand-mark__dot"></span>MB&amp;LR</div>
    </div>
  </section>

</body>
</html>
```